Book Cover Design Project

I would like a book cover designed for a book entitled: Bright Days Ahead: Finding the Right Cosmetic Dentist
The target audience is those patients interested in cosmetic dentistry. Generally those would be people over 45, with above average income, but the cover should have more universal appeal.
The book was written by
Raymond T. Oakes, DDS, FSFDP
Fellow in the Society of Family Dental Practice
(that's me)
The book will be distributed as an ebook for free to patients and potential patients interested in cosmetic dentistry.

```html
<!DOCTYPE html>
<html lang="en">
<head>
<meta charset="utf-8">
<title>Bright Days Ahead: Finding the Right Cosmetic Dentist</title>
<link rel="stylesheet" href="https://fonts.googleapis.com/css2?family=Rufina:wght@700&family=Chewy&family=Indie+Flower&family=Nunito:ital,wght@1,800&display=swap">
<style>
  :root {
    --peach: #fde1d7;
    --band: #ffffff;
    --coral: #f27a6b;
    --cyan: #22c3ec;
    --blue: #1aa3d6;
    --outline-grey: #b9b9b9;
  }
  * { margin: 0; padding: 0; box-sizing: border-box; }
  html, body { width: 894px; height: 1200px; overflow: hidden; }
  body { background: var(--peach); }
  .cover {
    position: relative;
    width: 894px;
    height: 1200px;
    background: var(--peach);
    overflow: hidden;
  }
  .title {
    position: absolute;
    left: 0;
    top: 18px;
    width: 830px;
    text-align: center;
    font-family: "Rufina", Georgia, serif;
    font-weight: 700;
    font-size: 178px;
    line-height: 182px;
    color: var(--coral);
    -webkit-text-stroke: 4px #fff;
    paint-order: stroke fill;
    text-shadow: 3px 4px 5px rgba(120, 60, 50, 0.35);
  }
  .title span { display: block; }
  .subtitle-band {
    position: absolute;
    left: 0;
    top: 596px;
    width: 894px;
    height: 177px;
    background: var(--band);
  }
  .subtitle {
    position: absolute;
    left: 0;
    top: 614px;
    width: 850px;
    text-align: center;
    font-family: "Chewy", "Comic Sans MS", sans-serif;
    font-weight: 400;
    font-size: 54px;
    line-height: 68px;
    color: #fff;
    -webkit-text-stroke: 5px var(--outline-grey);
    paint-order: stroke fill;
    text-shadow: 1px 2px 2px rgba(0,0,0,0.15);
  }
  .subtitle span { display: block; }
  .audience-tag {
    position: absolute;
    left: 605px;
    top: 612px;
    width: 356px;
    height: 356px;
  }
  .audience-tag svg { position: absolute; inset: 0; }
  .audience-tag p {
    position: absolute;
    left: 0;
    top: 58px;
    width: 356px;
    text-align: center;
    font-family: "Indie Flower", cursive;
    font-size: 28px;
    line-height: 38px;
    color: var(--cyan);
  }
  .tool-art {
    position: absolute;
    left: 30px;
    top: 812px;
    width: 575px;
    height: 138px;
    background: linear-gradient(90deg, rgba(200,200,200,0.25), rgba(230,227,225,0.8));
    border-radius: 60px 70px 70px 20px;
  }
  .rule {
    position: absolute;
    left: 60px;
    top: 988px;
    width: 752px;
    height: 3px;
    background: #fff;
    border-radius: 2px;
  }
  .author {
    position: absolute;
    left: 0;
    top: 1018px;
    width: 860px;
    text-align: center;
    font-family: "Nunito", Verdana, sans-serif;
    font-style: italic;
    font-weight: 800;
  }
  .author .name {
    display: block;
    font-size: 44px;
    line-height: 56px;
    color: var(--cyan);
  }
  .author .credential {
    display: block;
    font-size: 29px;
    line-height: 40px;
    color: var(--blue);
  }
</style>
</head>
<body>
  <main class="cover">
    <h1 class="title"><span>Bright</span><span>Days</span><span>Ahead</span></h1>

    <div class="subtitle-band"></div>
    <h2 class="subtitle"><span>Finding the Right</span><span>Cosmetic Dentist</span></h2>

    <div class="tool-art" role="img" aria-label="Illustration of a dental mirror lying flat"></div>

    <div class="audience-tag">
      <svg viewBox="0 0 356 356" width="356" height="356" aria-hidden="true">
        <polygon points="178,4 352,178 178,352 4,178" fill="#fff" stroke="#22c3ec" stroke-width="4"/>
      </svg>
      <p>For<br>potential<br>patients<br>interested<br>in cosmetic<br>dentistry.</p>
    </div>

    <div class="rule"></div>

    <p class="author">
      <span class="name">Raymond T. Oakes, DDS, FSFDP</span>
      <span class="credential">Fellow in the Society of Family Dental Practice</span>
    </p>
  </main>
</body>
</html>
```